Packaging & Label Design for CDB Products

We are a European CBD company specialising in athletic recovery, sleep improvement and wellness.

We would like the packaging to incorporate our logo and name (and font 'Codec') 'Lanternfield CBD'. The design must be transferable to all of our products. CBD Oils, Balms, Lip Balm and Vape E-Liquid.

We would like it to be simple but eye-catching and modern. We don't want bright colours. Preferred pallet of muted greys, blacks, white and pastel colours. Geometric concepts, possibly using different colours for each item of the range, we are open to new and fresh ideas (we are seeking you for your experience) and when we find the right design we would likely throw more work in your direction..

Our product range is not complete so the designer must be flexible with some changes and provide files where format can be easily edited by packaging manufacturer. We are also waiting for dimensions for the labels and boxes for several products and will supply the designer with full dimensions of all products once selected.

Oil Box: 2.6 x 9.0 x 2.6 cm (open format 16.7 x 11.6cm)
Labels: 7.8 x 3.3 cm (Front and Back)

Our expected product range will be:
CBD Oil 1000mg
CBD Oil 3000mg
CBD Balm 100mg
CBD Balm 300mg
E-Liquid 500mg
Lip Balm 50mg

We look forward to seeing your ideas.

Best Regards
Lanternfield CBD

```html
<!DOCTYPE html>
<html lang="en">
<head>
<meta charset="utf-8">
<title>Lanternfield CBD – Full Spectrum CBD Oil Packaging</title>
<link rel="stylesheet" href="https://fonts.googleapis.com/css2?family=Montserrat:wght@400;500;700&display=swap">
<style>
  :root {
    --backdrop: #f1f1f1;
    --paper: #ffffff;
    --ink: #1f1f1f;
    --leaf: #1f9a4c;
    --leaf-faint: #d6eadc;
    --edge: #e2e2e2;
  }
  * { box-sizing: border-box; margin: 0; padding: 0; }
  html, body {
    width: 1200px; height: 1200px; overflow: hidden;
    background: var(--backdrop);
    font-family: "Montserrat", "Helvetica Neue", Arial, sans-serif;
    color: var(--ink);
  }
  .canvas { position: relative; width: 1200px; height: 1200px; }

  .brand-dot { border-radius: 50%; background: var(--leaf); }
  .brand-name { font-weight: 700; text-align: center; color: var(--ink); }
  .backdrop-disc { position: absolute; border-radius: 50%; background: var(--leaf-faint); }

  /* Box front panel (2.6 x 9.0 cm) */
  .box-front {
    position: absolute; left: 130px; top: 145px;
    width: 330px; height: 910px;
    background: var(--paper);
    border: 1px solid var(--edge);
    overflow: hidden;
  }
  .box-front .brand-dot {
    position: absolute; left: 135px; top: 62px; width: 60px; height: 60px;
  }
  .box-front .brand-name {
    position: absolute; left: 0; right: 0; top: 150px;
    font-size: 24px; letter-spacing: 2px; line-height: 1.3;
  }
  .box-front .backdrop-disc {
    left: 120px; top: 270px; width: 240px; height: 340px; border-radius: 50%;
  }
  .box-front .product {
    position: absolute; left: 36px; right: 0; top: 635px;
  }
  .box-front .spectrum { font-size: 22px; color: var(--leaf); font-weight: 500; }
  .box-front .name { font-size: 52px; font-weight: 700; line-height: 1.05; margin-top: 2px; }
  .box-front .strength { font-size: 22px; color: var(--leaf); font-weight: 500; margin-top: 2px; }
  .box-front .extract { font-size: 20px; color: var(--leaf); font-weight: 500; margin-top: 46px; }
  .box-front .volume { font-size: 20px; font-weight: 500; margin-top: 10px; }

  /* Bottle label (7.8 x 3.3 cm), front centred */
  .bottle-label {
    position: absolute; left: 540px; top: 474px;
    width: 600px; height: 254px;
    background: var(--paper);
    border: 1px solid var(--edge);
  }
  .bottle-label .front {
    position: absolute; left: 170px; top: 0; width: 260px; height: 100%;
    overflow: hidden;
  }
  .bottle-label .brand-dot {
    position: absolute; left: 116px; top: 16px; width: 28px; height: 28px;
  }
  .bottle-label .brand-name {
    position: absolute; left: 0; right: 0; top: 52px;
    font-size: 14px; letter-spacing: 1.5px; line-height: 1.25;
  }
  .bottle-label .backdrop-disc {
    left: 215px; top: 125px; width: 90px; height: 120px;
  }
  .bottle-label .product { position: absolute; left: 34px; right: 0; top: 100px; }
  .bottle-label .spectrum { font-size: 14px; color: var(--leaf); font-weight: 500; }
  .bottle-label .name { font-size: 30px; font-weight: 700; line-height: 1.05; }
  .bottle-label .strength { font-size: 14px; color: var(--leaf); font-weight: 500; }
  .bottle-label .extract { font-size: 13px; color: var(--leaf); font-weight: 500; margin-top: 16px; }
  .bottle-label .volume { font-size: 13px; font-weight: 500; margin-top: 5px; }
</style>
</head>
<body>
<main class="canvas">
  <section class="box-front" aria-label="Carton front panel">
    <div class="backdrop-disc" aria-hidden="true"></div>
    <div class="brand-dot" aria-hidden="true"></div>
    <div class="brand-name">LANTERNFIELD<br>CBD</div>
    <div class="product">
      <p class="spectrum">Full Spectrum</p>
      <h1 class="name">CBD OIL</h1>
      <p class="strength">1000mg CBD</p>
      <p class="extract">10% Hemp Extract</p>
      <p class="volume">0.5 fl.oz | 10ml</p>
    </div>
  </section>

  <section class="bottle-label" aria-label="Bottle label">
    <div class="front">
      <div class="backdrop-disc" aria-hidden="true"></div>
      <div class="brand-dot" aria-hidden="true"></div>
      <div class="brand-name">LANTERNFIELD<br>CBD</div>
      <div class="product">
        <p class="spectrum">Full Spectrum</p>
        <h2 class="name">CBD OIL</h2>
        <p class="strength">1000mg CBD</p>
        <p class="extract">10% Hemp Extract</p>
        <p class="volume">0.5 fl.oz | 10ml</p>
      </div>
    </div>
  </section>
</main>
</body>
</html>
```